One of a kind service business!

We are the only ocean freight auditing company in the entire world that does what we do. We provide a innovative service in auditing our clients invoices for billing errors as it relates to the import and export of their products anywhere in the world. We'd like to retain the current logo - but we are open to any interesting concepts that can complete the card.

Target Market(s)

C-Level and Senior Financial executives

Industry/Entity Type

Auditing

Requirements
Must have

• ONE SIDED ONLY
Should not have
• no cartoonish images

```html
<!DOCTYPE html>
<html lang="en">
<head>
<meta charset="utf-8">
<title>Tidewater Review – Business Card</title>
<link href="https://fonts.googleapis.com/css2?family=Quicksand:wght@300;400;700&display=swap" rel="stylesheet">
<style>
  :root {
    --backdrop: #d9d6d2;
    --card-black: #0b0b0c;
    --card-sheen: #2a2b2e;
    --divider: #e9e9e9;
    --text-light: #c9c9c9;
    --text-white: #ffffff;
    --brand-blue: #8fd3f2;
  }
  * { margin: 0; padding: 0; box-sizing: border-box; }
  html, body {
    width: 1200px; height: 900px; overflow: hidden;
    background: var(--backdrop);
  }
  .canvas {
    position: relative; width: 1200px; height: 900px;
    display: flex; align-items: center; justify-content: center;
  }
  .business-card {
    position: relative; width: 960px; height: 670px;
    border-radius: 56px; overflow: hidden;
    background:
      linear-gradient(160deg, rgba(255,255,255,0.10) 0%, rgba(255,255,255,0.02) 38%, rgba(255,255,255,0) 39%),
      linear-gradient(180deg, var(--card-sheen) 0%, var(--card-black) 45%, var(--card-black) 100%);
    box-shadow: 0 18px 40px rgba(0,0,0,0.35);
    font-family: "Quicksand", sans-serif;
    color: var(--text-light);
  }
  .sheen-band {
    position: absolute; left: 0; top: 270px; width: 100%; height: 60px;
    background: linear-gradient(180deg, rgba(255,255,255,0) 0%, rgba(255,255,255,0.05) 50%, rgba(255,255,255,0) 100%);
  }
  .brand {
    position: absolute; left: 70px; top: 312px;
    display: flex; align-items: center; gap: 16px;
  }
  .brand-square {
    width: 34px; height: 34px; background: var(--brand-blue);
  }
  .brand-name {
    font-size: 40px; font-weight: 700; color: var(--brand-blue);
    letter-spacing: 0.5px; white-space: nowrap;
  }
  .divider {
    position: absolute; left: 500px; top: 100px;
    width: 3px; height: 530px; background: var(--divider);
  }
  .identity {
    position: absolute; left: 560px; top: 96px; width: 256px;
  }
  .person-name {
    font-size: 32px; font-weight: 700; color: var(--text-white);
    white-space: nowrap;
  }
  .person-title {
    font-size: 25px; font-weight: 300; text-align: right; margin-top: 2px;
  }
  .contact {
    position: absolute; left: 560px; top: 340px;
    font-size: 22px; font-weight: 300; line-height: 37px;
    list-style: none; white-space: nowrap;
  }
  .contact .label {
    font-weight: 700; color: var(--text-white); margin-right: 12px;
  }
</style>
</head>
<body>
<main class="canvas">
  <section class="business-card">
    <div class="sheen-band"></div>

    <div class="brand">
      <span class="brand-square"></span>
      <span class="brand-name">Tidewater Review</span>
    </div>

    <div class="divider"></div>

    <div class="identity">
      <p class="person-name">Daniel Marsh</p>
      <p class="person-title">CEO</p>
    </div>

    <ul class="contact">
      <li>Harbor Point Center, Linden Street 12</li>
      <li>Northport - Eastland 100 20</li>
      <li><span class="label">p</span>+555 210 184 136</li>
      <li><span class="label">m</span>+555 604 271 093</li>
      <li><span class="label">USA</span>+1 555 318 4026</li>
      <li><span class="label">f</span>+555 210 184 200</li>
      <li><span class="label">e</span>danielm@tidewaterreview.net</li>
      <li><span class="label">w</span>www.tidewaterreview.net</li>
    </ul>
  </section>
</main>
</body>
</html>
```